Self-Help & Training Association Business Card Design Project

We need double-sided business card for our Self-Help and Training Association called "Crescivento".

We want Zib.com to print them, both Orla and Standard Business Card format (**PLEASE DON'T SUBMIT ROUNDED-CORNERS CARDS).

(more info: http://uk.zibprint.example)

We ask designers to submit project based on our logo (attached) and color-set and to do it according to Zib.com designing guidelines.

We will print three variations (for three people) of the business card.

Let's apply now!

Thank you!

Target Market(s)

Common people

Industry/Entity Type

Business

Requirements
Must have
• Strings needed:

Association Name: Crescivento
Tagline: Formarsi per Vivere Meglio
Web: www.crescivento.it.example

Person Name: Sergio Bellandi
Person Title: Direttore Scientifico e Lead Trainer
Mobile: (+39) 347 5081923
E-mail: sergio@crescivento.it.example

Could be a nice idea to put general details on the front and personal details on the back of the card.

-
Artwork guidelines
You can use ZIB's online tools to position and crop your images, but if you'd like to pre-design your Business Cards, before you upload these are the dimensions you need:

Full bleed size
(Recommended for creating artwork - this includes the bleed, which will be cropped in production. Please note, you do not need to add crop marks to your artwork)

1039 x 697 pixels (300dpi)
88mm x 59mm (300dpi)
3.46" x 2.32" (300dpi)
Final size when trimmed
84mm x 55mm
3.30" x 2.16"
Accepted file types
We accept high resolution GIFs, PNGs, PDFs, and JPGs.

-

See http://www.crescivento.it.example/ for colors and style reference.

Thank you!
Nice to have
• If you still have empty space, this quote will be cool to be added:

"Non è il più forte o il più intelligente a sopravvivere, ma chi si adatta più velocemente al cambiamento. (F. Morvelli)"

```html
<!DOCTYPE html>
<html lang="it">
<head>
<meta charset="utf-8">
<title>Crescivento – Biglietto da visita</title>
<link rel="stylesheet" href="https://fonts.googleapis.com/css2?family=Ultra&family=Playfair+Display:ital,wght@1,700&family=Roboto+Condensed:wght@400;700&family=Arimo&display=swap">
<style>
  :root {
    --cyan: #2ff0f0;
    --magenta: #ff1493;
    --ink: #000000;
    --paper: #ffffff;
  }
  html, body {
    margin: 0;
    padding: 0;
    width: 1200px;
    height: 686px;
    overflow: hidden;
    background: var(--cyan);
  }
  .card {
    display: block;
    width: 1200px;
    height: 686px;
  }
  .brand-name {
    font-family: "Ultra", "Alfa Slab One", serif;
    font-size: 58px;
    letter-spacing: 6px;
    fill: var(--ink);
  }
  .quote {
    font-family: "Playfair Display", serif;
    font-style: italic;
    font-weight: 700;
    font-size: 36px;
    fill: var(--paper);
  }
  .tagline {
    font-family: "Roboto Condensed", sans-serif;
    font-size: 64px;
    fill: none;
    stroke: var(--ink);
    stroke-width: 1.6px;
  }
  .web-address {
    font-family: "Arimo", sans-serif;
    font-size: 46px;
    fill: var(--ink);
  }
  .person-name {
    font-family: "Roboto Condensed", sans-serif;
    font-weight: 700;
    font-size: 34px;
    fill: var(--paper);
  }
  .person-detail {
    font-family: "Roboto Condensed", sans-serif;
    font-weight: 400;
    font-size: 26px;
    fill: var(--paper);
  }
  .rule { stroke: var(--ink); stroke-width: 4; }
  .frame-line { stroke: var(--magenta); stroke-width: 9; }
</style>
</head>
<body>
<svg class="card" viewBox="0 0 1200 686" xmlns="http://www.w3.org/2000/svg">
  <defs>
    <radialGradient id="corner-shade" cx="0" cy="686" r="760" gradientUnits="userSpaceOnUse">
      <stop offset="0" stop-color="#000000"/>
      <stop offset="0.35" stop-color="#06393b"/>
      <stop offset="0.66" stop-color="#2ff0f0"/>
      <stop offset="1" stop-color="#2ff0f0"/>
    </radialGradient>
    <filter id="quote-drop" x="-5%" y="-20%" width="110%" height="140%">
      <feDropShadow dx="2" dy="2" stdDeviation="0.5" flood-color="#111"/>
    </filter>
  </defs>

  <rect class="background" x="0" y="0" width="1200" height="686" fill="var(--cyan)"/>
  <rect class="background-shade" x="0" y="0" width="1136" height="686" fill="url(#corner-shade)"/>

  <line class="frame-line" x1="0" y1="34" x2="1140" y2="34"/>
  <line class="frame-line" x1="1136" y1="0" x2="1136" y2="686"/>

  <text class="brand-name" x="617" y="122" text-anchor="middle">CRESCIVENTO</text>

  <line class="rule" x1="9" y1="238" x2="1126" y2="238"/>
  <line class="rule" x1="9" y1="311" x2="46" y2="311"/>
  <line class="rule" x1="1084" y1="311" x2="1126" y2="311"/>
  <line class="rule" x1="9" y1="377" x2="103" y2="377"/>
  <line class="rule" x1="1034" y1="377" x2="1126" y2="377"/>
  <line class="rule" x1="9" y1="443" x2="458" y2="443"/>
  <line class="rule" x1="678" y1="443" x2="1126" y2="443"/>

  <g class="quote" filter="url(#quote-drop)">
    <text x="36" y="300" textLength="1042" lengthAdjust="spacingAndGlyphs">"Non è il più forte o il più intelligente a sopravvivere, ma</text>
    <text x="111" y="366" textLength="904" lengthAdjust="spacingAndGlyphs">chi si adatta più velocemente al cambiamento. (F.</text>
    <text x="568" y="432" text-anchor="middle">Morvelli)"</text>
  </g>

  <g class="personal-details">
    <text class="person-name" x="24" y="508">Sergio Bellandi</text>
    <text class="person-detail" x="24" y="548">Direttore Scientifico e Lead Trainer</text>
    <text class="person-detail" x="24" y="588">(+39) 347 5081923</text>
    <text class="person-detail" x="24" y="628">sergio@crescivento.it.example</text>
  </g>

  <text class="tagline" x="548" y="577" textLength="572" lengthAdjust="spacingAndGlyphs">Formarsi per Vivere</text>
  <text class="tagline" x="834" y="663" text-anchor="middle">Meglio</text>

  <text class="web-address" transform="translate(1186 343) rotate(-90)" text-anchor="middle" textLength="620" lengthAdjust="spacingAndGlyphs">www.crescivento.it.example</text>
</svg>
</body>
</html>
```